Keystone Bookkeeping and Tax Services needs a postcard design for his business

Keystone Bookkeeping and Tax Services, specialize in helping small business owners to improve their financial position, maximize their profits as well as helps them to get their lives back. Through proper financial consultation a business can expect to save money on their taxes, use their cash flow effectively, and enjoy a higher return on their business. We would like to have photo of:1. small business owners, 2. an accountant that working. The final design should communicate that by hiring Keystone Bookkeeping and tax services they can concentrate doing their business and relax. Our tag line is "Maximizing your profit is our business". We have our logo already, using blue and orange. The color design should be match with our logo. I upload pictures of small business owner and a logo.
Thanks.

```html
<!DOCTYPE html>
<html lang="en">
<head>
<meta charset="utf-8">
<title>Keystone Bookkeeping and Tax Services – Postcard</title>
<link href="https://fonts.googleapis.com/css2?family=Roboto+Condensed:wght@300;400;700&display=swap" rel="stylesheet">
<style>
  :root {
    --backdrop: #505052;
    --card: #ffffff;
    --orange: #f37021;
    --orange-text: #f7941d;
    --blue: #23408e;
    --white: #ffffff;
    --ink: #231f20;
    --rule: #3a3a3a;
  }
  html, body {
    margin: 0;
    padding: 0;
    width: 1200px;
    height: 958px;
    overflow: hidden;
    background: var(--backdrop);
    font-family: "Roboto Condensed", "Arial Narrow", sans-serif;
  }
  .postcard {
    position: absolute;
    left: 75px;
    top: 76px;
    width: 1047px;
    height: 804px;
    background: var(--card);
  }
  .promo {
    position: absolute;
    left: 0;
    top: 0;
    width: 520px;
    height: 706px;
    border-bottom-right-radius: 20px;
    overflow: hidden;
  }
  .promo__header {
    position: absolute;
    left: 0; top: 0;
    width: 520px; height: 217px;
    background: var(--orange);
  }
  .promo__portrait {
    position: absolute;
    left: 25px; top: 17px;
    width: 205px; height: 200px;
    background: linear-gradient(180deg, #ffffff 0%, #fde3d2 100%);
    border-radius: 90px 90px 8px 8px;
  }
  .promo__name {
    position: absolute;
    right: 45px; top: 124px;
    margin: 0;
    color: var(--white);
    font-weight: 700;
    font-size: 42px;
    line-height: 1;
    text-align: right;
  }
  .promo__role {
    position: absolute;
    right: 55px; top: 175px;
    color: var(--white);
    font-weight: 300;
    font-size: 25px;
    line-height: 1;
  }
  .promo__body {
    position: absolute;
    left: 0; top: 217px;
    width: 520px; height: 366px;
    background: var(--blue);
  }
  .promo__bio {
    position: absolute;
    left: 55px; top: 27px;
    margin: 0;
    color: var(--white);
    font-weight: 300;
    font-size: 24px;
    line-height: 34.5px;
  }
  .promo__tagline {
    position: absolute;
    left: 50px; top: 214px;
    margin: 0;
    color: var(--orange-text);
    font-weight: 700;
    font-size: 38px;
    line-height: 42px;
  }
  .promo__cta {
    position: absolute;
    left: 0; top: 324px;
    width: 520px;
    text-align: center;
    color: var(--white);
    font-weight: 700;
    font-size: 30px;
    line-height: 1;
  }
  .promo__footer {
    position: absolute;
    left: 0; top: 583px;
    width: 520px; height: 123px;
    background: var(--orange);
    text-align: center;
    color: var(--white);
  }
  .promo__phone {
    display: block;
    margin-top: 13px;
    font-weight: 700;
    font-size: 58px;
    line-height: 62px;
  }
  .promo__web {
    display: block;
    font-weight: 400;
    font-size: 32px;
    line-height: 34px;
  }
  .promo__web strong { font-weight: 700; }

  .mailing {
    position: absolute;
    left: 547px; top: 42px;
    color: var(--ink);
  }
  .mailing__company {
    margin: 0 0 14px;
    color: var(--orange);
    font-weight: 700;
    font-size: 22px;
    line-height: 27px;
  }
  .mailing__row {
    display: flex;
    font-size: 21px;
    font-weight: 400;
    line-height: 26px;
    margin-bottom: 16px;
  }
  .mailing__row--tight { margin-bottom: 1px; }
  .mailing__label {
    font-weight: 700;
    width: 25px;
    flex: none;
  }
  .stamp-box {
    position: absolute;
    left: 898px; top: 42px;
    width: 108px; height: 123px;
    border: 1px solid var(--rule);
  }
  .address-line {
    position: absolute;
    left: 615px;
    width: 343px;
    border-top: 1px solid var(--rule);
  }
  .address-line--1 { top: 339px; }
  .address-line--2 { top: 401px; }
  .address-line--3 { top: 463px; }
</style>
</head>
<body>
  <div class="postcard">
    <section class="promo">
      <div class="promo__header">
        <div class="promo__portrait" role="img" aria-label="Silhouette of a business owner in suit and tie"></div>
        <h1 class="promo__name">DARA WEST,</h1>
        <div class="promo__role">OWNER/OPERATOR</div>
      </div>
      <div class="promo__body">
        <p class="promo__bio">Dara West, owner/operator of Keystone<br>Bookkeeping and Tax Services has provided<br>management, accounting and tax services<br>to small business owners for over 20 years.<br>Certifications and designations include:</p>
        <p class="promo__tagline">BALANCING YOUR<br>BUSINESS IS OUR BUSINESS</p>
        <div class="promo__cta">CALL NOW FOR MORE INFO</div>
      </div>
      <div class="promo__footer">
        <span class="promo__phone">(555) 014-2270</span>
        <span class="promo__web">WWW. <strong>KEYSTONEBOOKTAX</strong>.CA</span>
      </div>
    </section>

    <section class="mailing">
      <h2 class="mailing__company">KEYSTONE Bookkeeping<br>and Tax Services</h2>
      <div class="mailing__row"><span class="mailing__label">A :</span><span>18 Alder Crescent,<br>Eastbrook, ON. K0A 2B4</span></div>
      <div class="mailing__row mailing__row--tight"><span class="mailing__label">T :</span><span>(555) 014-2270</span></div>
      <div class="mailing__row"><span class="mailing__label">E :</span><span>dara@keystonebooktax.ca</span></div>
    </section>

    <div class="stamp-box"></div>
    <div class="address-line address-line--1"></div>
    <div class="address-line address-line--2"></div>
    <div class="address-line address-line--3"></div>
  </div>
</body>
</html>
```